Dane Calloway Photography

Would like the Business card to have a cool logo. I’m targeting wedding/ engagement: portrait photography. My phone number on it. And my business email address.

Target Market(s)

Wedding/portrait/engagement photography.

```html
<!DOCTYPE html>
<html lang="en">
<head>
<meta charset="utf-8">
<title>Dane Calloway Photography – Business Card</title>
<link href="https://fonts.googleapis.com/css2?family=Cinzel:wght@400&family=Arimo:wght@400&display=swap" rel="stylesheet">
<style>
  :root {
    --backdrop: #3a3330;
    --card: #0e0e0e;
    --card-edge: #1a1a1a;
    --pattern-deep: #161616;
    --pattern-light: #262626;
    --ink: #f2f2f2;
    --gold: #f3a82a;
    --rule: #6d6d6d;
  }
  * { margin: 0; padding: 0; box-sizing: border-box; }
  html, body {
    width: 1200px; height: 844px; overflow: hidden;
    background: var(--backdrop);
  }
  .stage {
    position: relative; width: 1200px; height: 844px;
    display: flex; align-items: center; justify-content: center; gap: 60px;
  }
  .card {
    position: relative; width: 520px; height: 297px;
    background: var(--card);
    border: 1px solid var(--card-edge);
    border-radius: 4px;
    box-shadow: 0 12px 30px rgba(0,0,0,.45);
    overflow: hidden;
    display: flex; flex-direction: column; align-items: center;
  }
  .brand {
    display: flex; align-items: center; gap: 10px;
    font-family: "Cinzel", serif; font-weight: 400;
    color: var(--ink); letter-spacing: 1px;
    font-size: 30px; line-height: 1;
  }
  .brand-dot {
    width: 16px; height: 16px; border-radius: 50%;
    background: var(--gold); flex: none;
  }
  .brand-sub {
    font-family: "Cinzel", serif; font-weight: 400;
    color: var(--ink); font-size: 15px; letter-spacing: 5px;
    margin-top: 8px;
  }
  .rule {
    width: 260px; height: 1px; background: var(--rule);
    margin-top: 12px;
  }
  /* front */
  .card-front { padding-top: 52px; }
  .holder {
    font-family: "Cinzel", serif; font-weight: 400;
    color: var(--gold); font-size: 19px; letter-spacing: 1px;
    margin-top: 16px;
  }
  .contact-icons { display: flex; gap: 5px; margin-top: 8px; }
  .contact-icons svg { width: 17px; height: 17px; display: block; }
  .contact-rule { width: 200px; margin-top: 8px; }
  .contact-list {
    list-style: none; margin-top: 8px; text-align: center;
    font-family: "Arimo", sans-serif; color: var(--ink);
    font-size: 15px; line-height: 21px;
  }
  /* back */
  .card-back { justify-content: center; }
  .card-back .pattern {
    position: absolute; inset: 0;
    background: radial-gradient(ellipse at center, var(--pattern-light), var(--pattern-deep) 75%);
  }
  .card-back .mark { position: relative; display: flex; flex-direction: column; align-items: center; }
</style>
</head>
<body>
<main class="stage">
  <section class="card card-front" aria-label="Business card front">
    <div class="brand"><span>Dane Calloway</span><span class="brand-dot"></span></div>
    <div class="brand-sub">Photography</div>
    <div class="rule"></div>
    <div class="holder">Marcus Hale</div>
    <div class="contact-icons" aria-hidden="true">
      <svg viewBox="0 0 20 20"><rect width="20" height="20" rx="2" fill="#f3a82a"/><path d="M6 4l3 3-2 2c1 2 2 3 4 4l2-2 3 3-2 2C9 16 4 11 4 6z" fill="#0e0e0e"/></svg>
      <svg viewBox="0 0 20 20"><rect width="20" height="20" rx="2" fill="#f3a82a"/><rect x="4" y="6" width="12" height="8" fill="#0e0e0e"/><path d="M4 6l6 5 6-5" stroke="#f3a82a" stroke-width="1.2" fill="none"/></svg>
      <svg viewBox="0 0 20 20"><rect width="20" height="20" rx="2" fill="#f3a82a"/><circle cx="10" cy="10" r="6" fill="#0e0e0e"/><path d="M4 10h12M10 4c-3 3-3 9 0 12M10 4c3 3 3 9 0 12" stroke="#f3a82a" stroke-width="1" fill="none"/></svg>
    </div>
    <div class="rule contact-rule"></div>
    <ul class="contact-list">
      <li>555-201-4388</li>
      <li>dane@danecallowayphoto.com</li>
      <li>www.danecallowayphoto.com</li>
    </ul>
  </section>

  <section class="card card-back" aria-label="Business card back">
    <div class="pattern" role="img" aria-label="Tonal pattern of cameras, lenses and film strips"></div>
    <div class="mark">
      <div class="brand"><span>Dane Calloway</span><span class="brand-dot"></span></div>
      <div class="brand-sub">Photography</div>
      <div class="rule"></div>
    </div>
  </section>
</main>
</body>
</html>
```